Business Card for Inovative Flexible Packaging Company

Create a business card that is both simple and stricking at the same time.
Preferably only one color (orange) or two colors (black and orange).
Information to print:
Torvalo, Lda
[T] 22 418 6093
[M] 91 326 7041
[F] 22 418 6135
[@] torvalo.ac@correiomx.com
SEDE & ARMAZÉM
Rua Das Figueiras do Monte, 312
Valmira
4795-832 Valmira - Corvelo
PORTUGAL
Reason: A lot of the ideas are obvious. I want something different. Inovative. dare to do something eye catching with style.
Business Consumers. Packaging Designers.
Business

```html
<!DOCTYPE html>
<html lang="pt">
<head>
<meta charset="utf-8">
<title>Torvalo — Business Card</title>
<link rel="stylesheet" href="https://fonts.googleapis.com/css2?family=Arimo:wght@400;700&display=swap">
<style>
  :root {
    --orange: #f26a21;
    --orange-light: #f7931e;
    --black: #111111;
    --black-soft: #1c1c1c;
    --white: #ffffff;
    --grey-text: #3a3a3a;
    --backdrop: #e6e7e4;
    --font: "Arimo", Arial, sans-serif;
  }
  * { box-sizing: border-box; margin: 0; padding: 0; }
  html, body {
    width: 1200px; height: 804px; overflow: hidden;
    background: var(--backdrop);
    font-family: var(--font);
  }
  .stage { position: relative; width: 1200px; height: 804px; }

  .card { position: absolute; box-shadow: 0 6px 18px rgba(0,0,0,.35); overflow: hidden; }

  /* Front face */
  .card-front {
    left: 0; top: 8px; width: 813px; height: 456px;
    background: radial-gradient(circle at 60% 40%, var(--black-soft), var(--black) 75%);
  }
  .front-mark {
    position: absolute; left: 70px; top: 98px;
    width: 300px; height: 300px; border-radius: 50%;
    background: linear-gradient(160deg, var(--orange-light), var(--orange));
  }
  .front-name {
    position: absolute; left: 410px; top: 168px;
    font-size: 78px; font-weight: 700; color: var(--orange);
    letter-spacing: -1px; line-height: 1;
  }
  .front-tagline {
    position: absolute; left: 414px; top: 274px;
    font-size: 17px; font-weight: 700; color: var(--white);
    letter-spacing: 4.3px;
  }

  /* Back face */
  .card-back {
    left: 372px; top: 346px; width: 778px; height: 452px;
    background: var(--white);
  }
  .back-header { position: absolute; left: 0; top: 0; width: 100%; height: 265px; }
  .back-mark {
    position: absolute; left: 38px; top: 40px;
    width: 58px; height: 58px; border-radius: 50%;
    background: linear-gradient(160deg, var(--orange-light), var(--orange));
  }
  .back-name {
    position: absolute; left: 110px; top: 38px;
    font-size: 58px; font-weight: 700; color: var(--orange); line-height: 1;
  }
  .back-tagline {
    position: absolute; left: 114px; top: 110px;
    font-size: 12.5px; color: var(--grey-text); letter-spacing: 3.3px;
  }
  .address {
    position: absolute; right: 22px; top: 72px; width: 300px;
    text-align: center; font-size: 14px; line-height: 1.3; color: var(--grey-text);
    font-style: normal;
  }
  .divider {
    position: absolute; left: 0; top: 265px; width: 100%; height: 3px;
    background: var(--orange);
  }
  .back-footer {
    position: absolute; left: 0; top: 268px; width: 100%; height: 184px;
    background: linear-gradient(180deg, var(--black-soft), var(--black));
    color: var(--white);
  }
  .company {
    position: absolute; left: 38px; top: 12px;
    font-size: 33px; font-weight: 400;
  }
  .contact {
    position: absolute; display: flex; align-items: center; gap: 16px;
    font-size: 20px;
  }
  .contact svg { width: 40px; height: 40px; flex: none; }
  .contact-phone { left: 36px; top: 66px; }
  .contact-mobile { left: 36px; top: 120px; }
  .contact-fax { right: 28px; top: 66px; }
  .contact-email { right: 28px; top: 120px; }
</style>
</head>
<body>
<main class="stage">

  <section class="card card-front" aria-label="Card front">
    <div class="front-mark" aria-hidden="true"></div>
    <div class="front-name">torvalo</div>
    <div class="front-tagline">FLEXIBLE PACK SYSTEMS</div>
  </section>

  <section class="card card-back" aria-label="Card back">
    <div class="back-header">
      <div class="back-mark" aria-hidden="true"></div>
      <div class="back-name">torvalo</div>
      <div class="back-tagline">FLEXIBLE PACK SYSTEMS</div>
      <address class="address">
        SEDE &amp; ARMAZÉM<br>
        Rua Das Figueiras do Monte, 312 Valmira<br>
        4795-832 Valmira - Corvelo PORTUGAL
      </address>
    </div>
    <div class="divider"></div>
    <div class="back-footer">
      <div class="company">Torvalo Lda</div>

      <div class="contact contact-phone">
        <svg viewBox="0 0 40 40" aria-label="Telefone">
          <path d="M11 6 L16 6 L18 14 L14 17 Q17 24 23 27 L26 23 L34 25 L34 30 Q33 35 28 34 Q12 30 6 13 Q6 7 11 6 Z" fill="none" stroke="var(--orange)" stroke-width="3" stroke-linejoin="round"/>
          <path d="M22 8 Q31 10 32 19 M22 13 Q27 14 27 19" fill="none" stroke="var(--orange)" stroke-width="2.5" stroke-linecap="round"/>
        </svg>
        <span>22 418 6093</span>
      </div>

      <div class="contact contact-mobile">
        <svg viewBox="0 0 40 40" aria-label="Telemóvel">
          <rect x="11" y="4" width="18" height="32" rx="3" fill="none" stroke="var(--orange)" stroke-width="3"/>
          <rect x="15" y="9" width="10" height="9" fill="var(--orange)"/>
          <g fill="var(--orange)">
            <rect x="15" y="22" width="3" height="3"/><rect x="21" y="22" width="3" height="3"/>
            <rect x="15" y="28" width="3" height="3"/><rect x="21" y="28" width="3" height="3"/>
          </g>
        </svg>
        <span>91 326 7041</span>
      </div>

      <div class="contact contact-fax">
        <span>22 418 6135</span>
        <svg viewBox="0 0 40 40" aria-label="Fax">
          <rect x="4" y="4" width="32" height="32" rx="2" fill="none" stroke="var(--orange)" stroke-width="3"/>
          <path d="M13 9 H27 V22 H13 Z M16 13 H24 M16 17 H24" fill="none" stroke="var(--orange)" stroke-width="2"/>
          <rect x="9" y="26" width="22" height="6" fill="var(--orange)"/>
        </svg>
      </div>

      <div class="contact contact-email">
        <span>torvalo.ac@correiomx.com</span>
        <svg viewBox="0 0 40 40" aria-label="Email">
          <rect x="4" y="9" width="32" height="22" fill="none" stroke="var(--orange)" stroke-width="3"/>
          <path d="M4 9 L20 22 L36 9 M4 31 L16 19 M36 31 L24 19" fill="none" stroke="var(--orange)" stroke-width="2.5"/>
        </svg>
      </div>
    </div>
  </section>

</main>
</body>
</html>
```